Velora "Glass Tide" single cover

We need a cover for Velora's New upcoming single "Glass Tide"
We have posted some Pictures and logo that we want you to work With. We need you to get her to look good :).The title is "Glass Tide" and is "Velora feat. Dorvo mint rascal"
The songs is a little hiphop/RnB (Marla Q'ish).
You can choose what colour you want for the logo and overall. But we don't want it to be gloomy.
watch www.velora-music.example or www.facebook.com/veloramusic
This is a digital release so we need only front page 12x12cm
Updates
If anyone wants to remove the background from the pictures and be creative that is fine! :)
Industry/Entity Type
Digital
Colors
Designer to choose colors to be used in the design.
Look and feel
Each slider illustrates characteristics of the customer's brand and the style your logo design should communicate.

```html
<!DOCTYPE html>
<html lang="en">
<head>
<meta charset="utf-8">
<title>Velora – Glass Tide</title>
<link href="https://fonts.googleapis.com/css2?family=Great+Vibes&display=swap" rel="stylesheet">
<style>
  :root {
    --paper: #f7f2e8;
    --title-red: #d9232e;
    --logo-orange: #f39a24;
    --portrait-red: #e8342c;
    --portrait-orange: #f28a3a;
    --portrait-yellow: #f5c94a;
    --portrait-pink: #ec8fa0;
    --portrait-light: #f6e7da;
  }
  html, body {
    margin: 0;
    padding: 0;
    overflow: hidden;
    background: var(--paper);
  }
  .cover {
    position: relative;
    width: 1200px;
    height: 1080px;
    overflow: hidden;
    background: var(--paper);
  }
  .cover__title {
    position: absolute;
    left: 70px;
    top: 22px;
    margin: 0;
    font-family: "Great Vibes", cursive;
    font-weight: 400;
    font-size: 68px;
    line-height: 1;
    color: var(--title-red);
  }
  .cover__artist {
    position: absolute;
    left: 153px;
    top: 585px;
    margin: 0;
    transform: translate(-50%, -50%) rotate(-90deg);
    font-family: "Great Vibes", cursive;
    font-weight: 400;
    font-size: 230px;
    line-height: 1;
    white-space: nowrap;
    color: var(--logo-orange);
  }
  .cover__portrait {
    position: absolute;
    left: 340px;
    top: 0;
    width: 860px;
    height: 1080px;
    background:
      radial-gradient(ellipse 38% 34% at 70% 42%, var(--portrait-light) 0%, rgba(246,231,218,0.85) 55%, rgba(246,231,218,0) 100%),
      radial-gradient(ellipse 45% 30% at 48% 20%, var(--portrait-yellow) 0%, rgba(245,201,74,0) 100%),
      radial-gradient(ellipse 40% 45% at 35% 55%, var(--portrait-pink) 0%, rgba(236,143,160,0) 100%),
      radial-gradient(ellipse 55% 55% at 55% 75%, var(--portrait-red) 0%, rgba(232,52,44,0) 100%),
      radial-gradient(ellipse 60% 70% at 60% 50%, var(--portrait-orange) 0%, rgba(242,138,58,0) 100%);
    -webkit-mask-image: radial-gradient(ellipse 62% 60% at 62% 48%, #000 55%, transparent 100%);
    mask-image: radial-gradient(ellipse 62% 60% at 62% 48%, #000 55%, transparent 100%);
  }
</style>
</head>
<body>
  <main class="cover">
    <div class="cover__portrait" role="img" aria-label="Watercolour-style portrait of the singer in red, orange, yellow and pink tones"></div>
    <h1 class="cover__title">Glass Tide</h1>
    <p class="cover__artist">Velora</p>
  </main>
</body>
</html>
```